Website design for learning and development business

I need a logo for my new business based in Australasia. I am a kiwi who is a creative change maker working in the Learning & development space. I design experiential learning opportunities for businesses to grow and nurture their tribes. I take a holistic look at an organisation and analyse what is needed to build a positive culture with a growth mindset woven into their DNA. I would like to see designs that are based on the following word snaps - creative, interesting, tribal, journey, adaptability, engaging, fluid, architectural, bespoke, courageous, challenging .I have the logo (attached) and I Need a startup business website designed. I am a Learning and development professional who is looking at going out on my own and establishing my own business. I would like a website designed that people would go to to check out what I do, how I do, what skills I have and how to contact me. Also room for a blog/articles.

Target Market(s)

Small to medium business

Industry/Entity Type

Self employed training and consultancy company

Number of Pages Required

5+ page

Requirements
Must have
• home page, about page, contact us page, blog page, search for us page
Nice to have
• Testimonials,

```html
<!DOCTYPE html>
<html lang="en">
<head>
<meta charset="utf-8">
<title>Verano Consulting</title>
<link rel="stylesheet" href="https://fonts.googleapis.com/css2?family=Cinzel:wght@700&family=Lato:ital,wght@0,400;0,700;0,900;1,400&display=swap">
<style>
:root{
  --accent:#e8542d;
  --blue:#347cc8;
  --blue-light:#5c98d8;
  --ink:#222;
  --body:#555;
  --light-bg:#f5f5f5;
  --grey-bg:#e6e6e6;
  --footer:#0b0b0b;
  --red:#d5121d;
  --navy:#1f1f75;
  --green:#2f9b2f;
  --rule:#bdbdbd;
}
*{margin:0;padding:0;box-sizing:border-box}
html,body{width:1200px;height:4030px;overflow:hidden;background:#fff}
body{font-family:'Lato',sans-serif;color:var(--body);position:relative}
.abs{position:absolute}
section,header,footer{position:absolute;left:0;width:1200px}
.section-title{position:absolute;left:0;width:1200px;display:flex;justify-content:center;align-items:center;gap:14px;font-family:'Cinzel',serif;font-weight:700;font-size:36px;color:var(--ink);letter-spacing:.5px;line-height:1}
.section-title::before,.section-title::after{content:"";width:105px;height:1px;background:var(--rule)}
.btn{position:absolute;display:flex;align-items:center;justify-content:center;font-family:'Lato',sans-serif;font-weight:700;font-size:16px;text-transform:uppercase}
.btn-accent{background:var(--accent);color:#fff}

/* header / hero */
.hero{top:0;height:698px;background:linear-gradient(180deg,#4a5056 0%,#3c4248 45%,#2c3136 80%,#23272b 100%)}
.hero-shade{position:absolute;inset:0;background:rgba(20,24,28,.35)}
.brand{position:absolute;left:111px;top:64px;color:#fff;font-family:'Lato',sans-serif;font-weight:900;line-height:1}
.brand .name{font-size:33px;letter-spacing:1px;display:block}
.brand .tag{font-size:11px;letter-spacing:6px;display:block;margin-top:4px;padding-left:40px}
.nav{position:absolute;top:74px;left:627px;display:flex;gap:48px;font-size:15px;color:#fff;text-transform:uppercase}
.nav .active{color:var(--accent);border-bottom:2px solid var(--accent);padding-bottom:8px}
.search{position:absolute;left:1073px;top:76px}
.hero-title{position:absolute;top:250px;width:1200px;text-align:center;font-family:'Cinzel',serif;font-weight:700;font-size:68px;color:#fff;letter-spacing:1px}
.hero-sub{position:absolute;top:330px;width:1200px;text-align:center;font-size:15px;color:#fff}
.hero .btn{left:522px;top:375px;width:155px;height:50px;border:2px solid #fff;color:#fff;font-weight:400;font-size:18px;text-transform:uppercase}
.dots{position:absolute;top:645px;left:566px;display:flex;gap:5px}
.dots span{width:14px;height:14px;border-radius:50%;border:2px solid #fff}
.dots span.on{background:#fff}

/* what i do */
.what{top:698px;height:466px;background:linear-gradient(180deg,#ffffff 0%,#f2f6fb 50%,#ffffff 100%)}
.what .section-title{top:62px}
.what-text{position:absolute;left:111px;width:978px;top:112px;text-align:center;font-size:13px;line-height:28px;color:#555}
.what-text p+p{margin-top:15px}
.what .btn{left:522px;top:342px;width:155px;height:50px}

/* how i do */
.how{top:1164px;height:624px;background:var(--blue)}
.how .section-title{top:72px;color:#fff}
.how .section-title::before,.how .section-title::after{background:var(--blue-light)}
.how-photo{position:absolute;left:111px;top:167px;width:552px;height:359px;border:9px solid var(--blue-light);background:linear-gradient(135deg,#dfe8f2 0%,#b9c8d8 40%,#8fa2b6 70%,#e8eef4 100%)}
.how-text{position:absolute;left:706px;top:172px;width:381px;font-size:12.5px;line-height:25px;color:#fff}
.how-text p+p{margin-top:10px}
.how .btn{left:706px;top:460px;width:144px;height:50px;background:#fff;color:var(--blue);font-weight:400}

/* skills */
.skills{top:1788px;height:474px;background:#fff}
.skills .section-title{top:62px}
.skill{position:absolute;top:155px;width:190px;text-align:center;font-size:21px;color:#222;text-transform:uppercase}
.skill .ring{width:190px;height:190px;border-radius:50%;display:flex;align-items:center;justify-content:center;margin-bottom:18px}
.skill .ring .core{width:178px;height:178px;border-radius:50%;border:3px solid #fff;display:flex;align-items:center;justify-content:center}

/* articles */
.articles{top:2262px;height:567px;background:var(--light-bg)}
.articles .section-title{top:66px}
.card{position:absolute;top:151px;width:303px}
.card .photo{position:relative;width:303px;height:173px}
.card .date{position:absolute;left:0;bottom:0;width:113px;height:34px;background:var(--blue);color:#fff;font-size:10px;display:flex;align-items:center;padding-left:12px}
.card h3{font-weight:400;font-size:17px;line-height:21px;color:#222;margin-top:16px}
.card p{font-size:12.5px;line-height:20px;color:#555;margin-top:16px;padding-left:2px}
.card a{display:block;margin-top:18px;font-weight:700;font-size:15px;color:var(--accent);text-decoration:underline}
.chev{position:absolute}

/* testimonials */
.testimonials{top:2829px;height:358px;background:var(--grey-bg)}
.testimonials .section-title{top:64px}
.avatar{position:absolute;left:223px;top:145px;width:132px;height:132px;border-radius:50%;border:4px solid #fff;background:radial-gradient(circle at 50% 40%,#c87a5c 0%,#a14a33 55%,#6b2c20 100%);box-shadow:0 0 0 1px #ccc}
.quote{position:absolute;left:394px;top:172px;width:570px;font-style:italic;font-size:16px;line-height:26px;color:#555}
.quote-name{position:absolute;left:394px;top:256px;font-weight:700;font-size:16px;color:var(--accent)}

/* contact */
.contact{top:3187px;height:513px;background:#fff}
.contact .section-title{top:72px}
.info{position:absolute;left:111px;display:flex;gap:9px;font-size:14.5px;line-height:23px;color:#333}
.info svg{flex:none;margin-top:4px}
.field{position:absolute;border:1px solid #d8d8d8;background:#fff;font-size:13px;color:#666;padding:10px 13px}
.contact .btn{left:496px;top:400px;width:145px;height:47px;font-size:15px}

/* footer */
.site-footer{top:3700px;height:330px;background:var(--footer);color:#fff}
.site-footer .brand{left:111px;top:77px}
.site-footer .brand .name{font-size:30px}
.site-footer .brand .tag{font-size:10px;padding-left:34px}
.social{position:absolute;left:155px;top:176px;display:flex;gap:9px}
.social span{width:34px;height:34px;border-radius:50%;background:#2a2a2a;border:1px solid #3a3a3a}
.foot-head{position:absolute;top:56px;font-family:'Cinzel',serif;font-weight:700;font-size:15px;letter-spacing:1px}
.foot-links{position:absolute;top:97px;list-style:none;font-size:12.5px;line-height:30.5px}
.foot-contact{position:absolute;left:834px;top:97px;width:260px;font-size:12.5px;line-height:22px}
.foot-contact div{display:flex;gap:6px}
.foot-contact .phone{margin-top:16px;font-size:15px}
.foot-rule{position:absolute;left:111px;top:255px;width:978px;height:1px;background:#333}
.copy{position:absolute;top:284px;width:1200px;text-align:center;font-size:11px;color:#ddd}
</style>
</head>
<body>

<header class="hero">
  <div class="abs" style="inset:0" role="img" aria-label="Photo of a businessman standing at a window overlooking a city skyline, glasses on a table in the foreground"></div>
  <div class="hero-shade"></div>
  <div class="brand"><span class="name">VERANO</span><span class="tag">CONSULTING</span></div>
  <nav class="nav"><span class="active">Home</span><span>About</span><span>Blog</span><span>Contact</span></nav>
  <svg class="search" width="15" height="15" viewBox="0 0 15 15"><circle cx="6" cy="6" r="4.5" fill="none" stroke="#fff" stroke-width="2"/><line x1="9.5" y1="9.5" x2="13.5" y2="13.5" stroke="#fff" stroke-width="2.2"/></svg>
  <h1 class="hero-title">VERANO CONSULTING</h1>
  <p class="hero-sub">I am a Learning and development professional who is looking at going out on my own and establishing my own business</p>
  <a class="btn">Learn More</a>
  <div class="dots"><span class="on"></span><span></span><span></span><span></span></div>
</header>

<section class="what">
  <h2 class="section-title">What I Do</h2>
  <div class="what-text">
    <p>Lorem ipsum dolor sit amet, consectetur adipiscing elit, sed do eiusmod tempor incididunt ut labore et dolore magna aliqua. Ut enim ad minim veniam, quis nostrud exercitation ullamco laboris nisi ut aliquip ex ea commodo consequat. Duis aute irure dolor in reprehenderit in voluptate velit esse cillum dolore eu fugiat nulla pariatur sint occaecat cupidatat non proident, sunt in culpa qui officia deserunt mollit anim id est laborum</p>
    <p>Sed ut perspiciatis unde omnis iste natus error sit voluptatem accusantium doloremque laudantium, totam rem aperiam, eaque ipsa quae ab illo inventore veritatis et quasi architecto beatae vitae dicta sunt explicabo. Nemo enim ipsam voluptatem quia voluptas sit aspernatur aut odit aut fugit, sed quia consequuntur magni dolores eos qui ratione voluptatem sequi nesciunt.</p>
  </div>
  <a class="btn btn-accent">Read More</a>
</section>

<section class="how">
  <h2 class="section-title">How I Do</h2>
  <div class="how-photo" role="img" aria-label="Photo of hands signing a document with a pen beside a tablet"></div>
  <div class="how-text">
    <p>But I must explain to you how all this mistaken idea of denouncing pleasure and praising pain was born and I will give you a complete account of the system, and expound the actual teachings of the great explorer of the truth, the master-builder of human happiness. No one rejects, dislikes, or avoids pleasure itself, because it is pleasure, but because those who do not know how to pursue pleasure.</p>
    <p>Nor again is there anyone who loves or pursues or desires to obtain pain of itself, because it is pain, but because occasionally circumstances occur in which toil and pain can procure.</p>
  </div>
  <a class="btn">Learn More</a>
</section>

<section class="skills">
  <h2 class="section-title">What Skills I Have</h2>
  <div class="skill" style="left:171px">
    <div class="ring" style="background:var(--red)"><div class="core">
      <svg width="90" height="90" viewBox="0 0 90 90" fill="none" stroke="#fff" stroke-width="2.5"><path d="M30 82V66c-10-6-14-16-12-28C21 20 36 10 52 12c16 2 26 16 24 32l6 12h-7v10c0 6-4 8-10 8h-7v8"/><circle cx="47" cy="38" r="11"/><circle cx="47" cy="38" r="4"/></svg>
    </div></div>Learning</div>
  <div class="skill" style="left:512px">
    <div class="ring" style="background:var(--navy)"><div class="core">
      <svg width="90" height="90" viewBox="0 0 90 90" fill="none" stroke="#fff" stroke-width="2.5"><path d="M24 12l21 10 21-10-8 14H32z"/><path d="M38 26l-8 40 15 16 15-16-8-40"/></svg>
    </div></div>Professional</div>
  <div class="skill" style="left:837px">
    <div class="ring" style="background:var(--green)"><div class="core">
      <svg width="90" height="90" viewBox="0 0 90 90" fill="none" stroke="#fff" stroke-width="2.5"><rect x="18" y="10" width="50" height="70" rx="3"/><circle cx="43" cy="30" r="9"/><line x1="28" y1="50" x2="58" y2="50"/><line x1="28" y1="58" x2="58" y2="58"/><line x1="28" y1="66" x2="48" y2="66"/><path d="M60 74l14-20 4 3-14 20-6 2z"/></svg>
    </div></div>Development</div>
</section>

<section class="articles">
  <h2 class="section-title">Latest Articles</h2>
  <svg class="chev" style="left:48px;top:224px" width="24" height="46" viewBox="0 0 24 46"><path d="M22 2L3 23l19 21" fill="none" stroke="#999" stroke-width="2"/></svg>
  <svg class="chev" style="left:1111px;top:224px" width="24" height="46" viewBox="0 0 24 46"><path d="M2 2l19 21L2 44" fill="none" stroke="#999" stroke-width="2"/></svg>
  <article class="card" style="left:111px">
    <div class="photo" role="img" aria-label="Photo of two business people shaking hands" style="background:linear-gradient(135deg,#e8ecef 0%,#c7ced6 50%,#5b6470 100%)"><span class="date">APRIL 30, 2021</span></div>
    <h3>Finibus Bonorum et Malorum the Extremes of Good and Evil</h3>
    <p>Lorem ipsum dolor sit amet, consectetur adipiscing elit, sed do eiusmod tempor incididunt ut labore et dolore magna aliqua</p>
    <a>READ MORE</a>
  </article>
  <article class="card" style="left:449px">
    <div class="photo" role="img" aria-label="Photo of colleagues reviewing documents at a desk" style="background:linear-gradient(135deg,#3d6fa3 0%,#9cb6cf 45%,#e9e2d6 100%)"><span class="date">March 19, 2021</span></div>
    <h3>Finibus Bonorum et Malorum the Extremes of Good and Evil</h3>
    <p>Lorem ipsum dolor sit amet, consectetur adipiscing elit, sed do eiusmod tempor incididunt ut labore et dolore magna aliqua</p>
    <a>READ MORE</a>
  </article>
  <article class="card" style="left:785px">
    <div class="photo" role="img" aria-label="Photo of a laptop with overlaid data charts" style="background:linear-gradient(135deg,#1e3f66 0%,#3b6898 50%,#7ea3c8 100%)"><span class="date">APRIL 4, 2021</span></div>
    <h3>Finibus Bonorum et Malorum the Extremes of Good and Evil</h3>
    <p>Lorem ipsum dolor sit amet, consectetur adipiscing elit, sed do eiusmod tempor incididunt ut labore et dolore magna aliqua</p>
    <a>READ MORE</a>
  </article>
</section>

<section class="testimonials">
  <h2 class="section-title">Testimonials</h2>
  <svg class="chev" style="left:110px;top:197px" width="18" height="32" viewBox="0 0 18 32"><path d="M16 2L3 16l13 14" fill="none" stroke="#888" stroke-width="2"/></svg>
  <svg class="chev" style="left:1066px;top:197px" width="18" height="32" viewBox="0 0 18 32"><path d="M2 2l13 14L2 30" fill="none" stroke="#888" stroke-width="2"/></svg>
  <div class="avatar" role="img" aria-label="Portrait photo of the client giving the testimonial"></div>
  <p class="quote">At vero eos et accusamus et iusto odio dignissimos ducimus qui blanditiis praesentium voluptatum deleniti atque corrupti quos dolores et quas molestias excepturi sint occaecati cupiditate non provident.</p>
  <span class="quote-name">“Mira”</span>
</section>

<section class="contact">
  <h2 class="section-title">Contact Me</h2>
  <div class="info" style="top:168px"><svg width="13" height="18" viewBox="0 0 13 18"><path d="M6.5 0C2.9 0 0 2.8 0 6.4 0 11 6.5 18 6.5 18S13 11 13 6.4C13 2.8 10.1 0 6.5 0z" fill="var(--accent)"/><circle cx="6.5" cy="6.4" r="2.4" fill="#fff"/></svg><span>Verano, 48 Harbour Lane #12<br>Wellington, NZ 6011</span></div>
  <div class="info" style="top:258px"><svg width="15" height="15" viewBox="0 0 15 15"><path d="M3 0l3 4-2 2c1 2 3 4 5 5l2-2 4 3-2 3C6 15 0 9 0 3z" fill="var(--accent)"/></svg><span>021.555.0148</span></div>
  <div class="info" style="top:317px"><svg width="16" height="12" viewBox="0 0 16 12"><rect width="16" height="12" rx="1" fill="var(--accent)"/><path d="M0 1l8 6 8-6" fill="none" stroke="#fff" stroke-width="1.3"/></svg><span>hello@veranoconsulting.example</span></div>
  <div class="field" style="left:496px;top:169px;width:292px;height:39px">Your name</div>
  <div class="field" style="left:796px;top:169px;width:291px;height:39px">Phone number</div>
  <div class="field" style="left:496px;top:228px;width:591px;height:39px">Email</div>
  <div class="field" style="left:496px;top:288px;width:591px;height:90px">Your message</div>
  <a class="btn btn-accent">Submit Now</a>
</section>

<footer class="site-footer">
  <div class="brand"><span class="name">VERANO</span><span class="tag">CONSULTING</span></div>
  <div class="social"><span></span><span></span><span></span></div>
  <h4 class="foot-head" style="left:422px">LINKS</h4>
  <ul class="foot-links" style="left:422px"><li>Home</li><li>About</li><li>Contact</li><li>Blog</li></ul>
  <ul class="foot-links" style="left:620px"><li>Our Clients</li><li>Terms of Use</li><li>Privacy Policy</li></ul>
  <h4 class="foot-head" style="left:834px">CONTACT DETAILS</h4>
  <div class="foot-contact">
    <div><svg width="10" height="14" viewBox="0 0 13 18" style="margin-top:4px;flex:none"><path d="M6.5 0C2.9 0 0 2.8 0 6.4 0 11 6.5 18 6.5 18S13 11 13 6.4C13 2.8 10.1 0 6.5 0z" fill="#fff"/></svg><span>Verano, 48 Harbour Lane #12 Wellington, NZ 6011</span></div>
    <div class="phone"><svg width="12" height="12" viewBox="0 0 15 15" style="margin-top:5px;flex:none"><path d="M3 0l3 4-2 2c1 2 3 4 5 5l2-2 4 3-2 3C6 15 0 9 0 3z" fill="#fff"/></svg><span>021.555.0148</span></div>
  </div>
  <div class="foot-rule"></div>
  <p class="copy">Copyright © 2021 Verano. All rights reserved.</p>
</footer>

</body>
</html>
```